Relationship Seminar

I am an Author and Speaker and I need a flyer for a Christian relationship seminar targeting women aged between mid 20's to late 30's. It's an event for women only.

-I am looking for a fresh/ edgy look but still feminine
-Nothing too girly
-Maximum of 3 colours (Spring colours are good)
-I want the flyer to convey joy or happiness
-Use my photo which is attached as the predominant image (you can crop it to remove the background etc)

The Flyer Details are as follows:

Somewhere Along The Way - Brisbane Tour

Join Author & Speaker, Rosalind Kupferle, as she speaks about her new book entitled 'Somewhere Along The Way'.

Be inspired and encouraged to embrace the life that God has given you and make the most of it!

Date: Saturday 9th November 2013
Time: 2:00 pm - 5:00 pm
Location: Harwick Lodge Brisbane (Juniper Hall)
Pelham Crescent, Brisbane QLD 4000
Tickets: $60/pp (Includes High Tea)
Buy Tickets: www.rosalindkupferle.com or http://somewherealongtheway.ticketquarry.net

Email: info@rosalindkupferle.com

Include the cover of my new book.

www.rosalindkupferle.com (include my website at the bottom of the flyer)

Target Market(s)

Young professional women aged between their mid 20's to late 30's

Industry/Entity Type

Event

Requirements
Should not have
• -No girly or curly font

```html
<!DOCTYPE html>
<html lang="en">
<head>
<meta charset="utf-8">
<title>Somewhere Along The Way – Brisbane Tour</title>
<link href="https://fonts.googleapis.com/css2?family=Roboto+Condensed:wght@400;700&family=Open+Sans:wght@400;600;700&display=swap" rel="stylesheet">
<style>
  :root {
    --red: #b3141c;
    --red-deep: #8a0d13;
    --red-bright: #d0202a;
    --ink: #2b2b2b;
    --slate: #3f3f3f;
    --paper: #f6f6f6;
    --paper-shade: #cdcdcd;
    --white: #ffffff;
    --rule: #c84a4f;
  }
  * { box-sizing: border-box; margin: 0; padding: 0; }
  html, body { width: 715px; height: 1200px; overflow: hidden; background: var(--white); }
  .flyer {
    position: relative; width: 715px; height: 1200px; overflow: hidden;
    background: linear-gradient(180deg, var(--paper) 0%, #e2e2e2 24%, var(--paper) 56%, var(--paper-shade) 88%);
    font-family: "Open Sans", Arial, sans-serif; color: var(--ink);
  }
  .headline { position: absolute; top: 14px; left: 0; width: 100%; text-align: center; font-family: "Roboto Condensed", "Arial Narrow", sans-serif; }
  .headline .title { color: var(--red); font-weight: 700; font-size: 86px; line-height: 90px; letter-spacing: -0.5px; }
  .headline .tour { color: var(--slate); font-weight: 700; font-size: 58px; line-height: 66px; margin-top: 14px; }
  .intro {
    position: absolute; top: 330px; left: 0; width: 100%; height: 88px;
    background: var(--red); color: var(--white);
    font-family: "Roboto Condensed", "Arial Narrow", sans-serif; font-size: 17.5px; line-height: 21px;
    padding: 12px 22px 0 22px;
  }
  .feature {
    position: absolute; top: 424px; left: 0; width: 100%; height: 252px;
  }
  .feature .portrait { position: absolute; inset: 0; width: 100%; height: 100%; }
  .feature .book-cover { position: absolute; left: 146px; top: 14px; width: 144px; height: 176px; }
  .feature .tagline {
    position: absolute; left: 22px; top: 188px; font-family: "Roboto Condensed", sans-serif;
    font-weight: 700; color: var(--red-bright); font-size: 30px; letter-spacing: 1px; text-transform: uppercase;
  }
  .feature .tagline-sub { position: absolute; left: 46px; top: 226px; color: var(--white); font-size: 13px; }
  .details { position: absolute; top: 692px; left: 0; width: 100%; text-align: center; font-size: 25px; font-weight: 700; line-height: 34px; }
  .details .label { color: var(--red); }
  .details .row { padding: 3px 0; }
  .details .rule { width: 560px; height: 1px; background: var(--rule); margin: 2px auto; }
  .email {
    position: absolute; top: 923px; left: 190px; width: 336px; height: 38px; border-radius: 19px;
    background: linear-gradient(90deg, var(--red) 0%, var(--red-deep) 100%);
    color: var(--white); text-align: center; line-height: 38px; font-size: 20px; font-weight: 600;
  }
  .email small { font-size: 12px; margin-right: 4px; }
  .social { position: absolute; top: 968px; height: 58px; display: flex; align-items: center; gap: 6px; font-weight: 700; font-size: 15px; color: var(--slate); }
  .social .mark { width: 14px; height: 14px; background: var(--slate); }
  .social.left { left: 22px; }
  .social.right { left: 570px; }
  .tickets {
    position: absolute; top: 962px; left: 225px; width: 264px; height: 68px; border-radius: 14px;
    background: var(--white); border: 1px solid #9a9a9a; text-align: center;
  }
  .tickets .price-line { margin-top: 4px; font-size: 30px; font-weight: 700; color: var(--red); line-height: 40px; }
  .tickets .price-line .amount { color: var(--ink); font-size: 38px; letter-spacing: -1px; }
  .tickets .note { font-size: 10px; font-style: italic; color: var(--slate); margin-top: -4px; }
  .footer-band { position: absolute; left: 0; top: 1060px; width: 715px; height: 140px; }
  .footer-text { position: absolute; top: 1092px; left: 0; width: 100%; text-align: center; color: var(--white); font-weight: 700; }
  .footer-text .cta { font-size: 25px; line-height: 34px; }
  .footer-text .url { font-size: 19px; line-height: 25px; letter-spacing: 0.4px; }
</style>
</head>
<body>
<main class="flyer">
  <header class="headline">
    <h1 class="title">Somewhere Along<br>The Way</h1>
    <p class="tour">Brisbane Tour</p>
  </header>

  <p class="intro">Join Author &amp; Speaker, Rosalind Kupferle, as she speaks about her new book entitled 'Somewhere Along The Way'. Be inspired and encouraged to embrace the life that God has given you and make the most of it!</p>

  <section class="feature">
    <svg class="portrait" viewBox="0 0 715 252" preserveAspectRatio="none" role="img" aria-label="Photograph of the smiling author in a dark jacket against a softly blurred brick wall">
      <defs>
        <linearGradient id="wallTone" x1="0" y1="0" x2="1" y2="0">
          <stop offset="0" stop-color="#d9cfcc"/>
          <stop offset="0.5" stop-color="#b9a19c"/>
          <stop offset="0.75" stop-color="#4a3a36"/>
          <stop offset="1" stop-color="#2a2321"/>
        </linearGradient>
      </defs>
      <rect width="715" height="252" fill="url(#wallTone)"/>
    </svg>
    <svg class="book-cover" viewBox="0 0 144 176" role="img" aria-label="Cover of the book Somewhere Along The Way">
      <rect width="144" height="176" fill="#eeeeee" stroke="#bdbdbd"/>
    </svg>
    <p class="tagline">Live Love Laugh</p>
    <p class="tagline-sub">A Must Read For Single Women</p>
  </section>

  <section class="details">
    <p class="row"><span class="label">Date:</span> Saturday 9th November 2013</p>
    <div class="rule"></div>
    <p class="row"><span class="label">Time:</span>&nbsp; 2:00 pm - 5:00 pm</p>
    <div class="rule"></div>
    <p class="row"><span class="label">Location:</span> Harwick Lodge Brisbane<br>(Juniper Hall), Pelham Crescent,<br>Brisbane QLD 4000</p>
  </section>

  <p class="email"><small>Email:</small>info@rosalindkupferle.com</p>

  <p class="social left"><span class="mark"></span>Friendsy</p>
  <div class="tickets">
    <p class="price-line">Tickets: <span class="amount">$60</span>/pp</p>
    <p class="note">(includes High Tea)</p>
  </div>
  <p class="social right"><span class="mark"></span>Chirper</p>

  <svg class="footer-band" viewBox="0 0 715 140" preserveAspectRatio="none" aria-hidden="true">
    <defs>
      <linearGradient id="bandRed" x1="0" y1="0" x2="1" y2="0">
        <stop offset="0" stop-color="#8a0d13"/>
        <stop offset="0.5" stop-color="#c41a23"/>
        <stop offset="1" stop-color="#8a0d13"/>
      </linearGradient>
    </defs>
    <path d="M0 24 Q357 -6 715 24 L715 36 Q357 6 0 36 Z" fill="#8c8c8c"/>
    <path d="M0 32 Q357 2 715 32 L715 140 L0 140 Z" fill="url(#bandRed)"/>
  </svg>
  <div class="footer-text">
    <p class="cta">Buy Tickets:</p>
    <p class="url">www.rosalindkupferle.com</p>
    <p class="url">http://somewherealongtheway.ticketquarry.net</p>
  </div>
</main>
</body>
</html>
```